Business Card & Word Docs from existing Logo

We need a business card with typical information plus layout to include electrical contractors license number, VORLE license and KMT license. We would like a word document layout for a proposal document, opening page with logo and design basic information; proposal to and proposal from and project name and number. Small basic single page letter for general documents. Email signature with logo.

We are an electrical, refrigeration and automation contractor. We work with reducing energy consumption for our customers and complex process solutions in electrical, refrigeration and automation.
Updates

Reason: Final changes/ revisions to designs.

Target Market(s)

Industrial and commercial businesses that require more than your average contractor.

Industry/Entity Type

Electrical

Requirements
Must have
• Propsal document must have a full opening page.

```html
<!DOCTYPE html>
<html lang="en">
<head>
<meta charset="utf-8">
<title>Frostline Contracting – Proposal Cover &amp; Letterhead</title>
<link rel="stylesheet" href="https://fonts.googleapis.com/css2?family=Arimo:wght@400;700&display=swap">
<style>
  :root {
    --backdrop: #e4e4e4;
    --paper: #ffffff;
    --ink: #111111;
    --label-blue: #1f68b0;
    --label-green: #2b8a3c;
    --title-lime: #d6e28e;
    --rule: #a8a8a8;
    --streak-green: #2f8a3e;
    --streak-teal: #2f8f8c;
    --streak-blue: #2c62a8;
    --streak-navy: #1b2b6b;
    --brand-blue: #1b75b8;
  }
  * { box-sizing: border-box; margin: 0; padding: 0; }
  html, body { width: 1200px; height: 900px; overflow: hidden; }
  body {
    position: relative;
    background: var(--backdrop);
    font-family: "Arimo", Arial, sans-serif;
    color: var(--ink);
  }
  .page { position: absolute; background: var(--paper); overflow: hidden; }
  .cover { left: 34px; top: 24px; width: 656px; height: 849px; }
  .letterhead { left: 721px; top: 307px; width: 437px; height: 566px; }

  .streaks {
    position: absolute; left: 0; width: 100%;
    background:
      linear-gradient(115deg, transparent 0 38%, rgba(255,255,255,.25) 44%, transparent 52% 70%, rgba(255,255,255,.18) 76%, transparent 84%),
      linear-gradient(105deg, var(--streak-green) 0%, var(--streak-teal) 25%, var(--streak-blue) 50%, var(--streak-navy) 78%, var(--streak-blue) 100%);
  }
  .cover .streaks-top { top: 0; height: 470px;
    -webkit-mask-image: linear-gradient(to bottom, #000 0 68%, transparent 100%);
            mask-image: linear-gradient(to bottom, #000 0 68%, transparent 100%); }
  .cover .streaks-bottom { bottom: 0; height: 130px; opacity: .85;
    -webkit-mask-image: linear-gradient(to top, #000 0 35%, transparent 100%);
            mask-image: linear-gradient(to top, #000 0 35%, transparent 100%); }
  .letterhead .streaks-top { top: 0; height: 110px;
    -webkit-mask-image: linear-gradient(to bottom, #000 0 50%, transparent 100%);
            mask-image: linear-gradient(to bottom, #000 0 50%, transparent 100%); }

  .brand-tab {
    position: absolute; background: var(--paper);
    display: flex; align-items: center;
  }
  .cover .brand-tab { left: 0; top: 58px; width: 376px; height: 105px; border-radius: 0 14px 14px 0; padding-left: 52px; gap: 14px; }
  .letterhead .brand-tab { left: 1px; top: 18px; width: 104px; height: 27px; border-radius: 0 4px 4px 0; padding-left: 10px; gap: 4px; }
  .brand-dot { border-radius: 50%; background: var(--brand-blue); flex: none; }
  .cover .brand-dot { width: 46px; height: 46px; }
  .letterhead .brand-dot { width: 12px; height: 12px; }
  .brand-name { color: var(--brand-blue); font-weight: 700; line-height: 1.05; letter-spacing: .5px; }
  .cover .brand-name { font-size: 25px; }
  .letterhead .brand-name { font-size: 7px; }

  .project { position: absolute; right: 45px; text-align: right; color: var(--paper); }
  .cover .project-title { top: 200px; font-size: 24px; font-weight: 700; color: var(--title-lime); line-height: 28px; }
  .cover .project-ref { top: 262px; font-size: 18px; }
  .cover .project-date { top: 304px; font-size: 19px; line-height: 24px; }
  .project-date strong { font-weight: 700; }

  .party { position: absolute; top: 478px; font-size: 14px; line-height: 17.4px; }
  .party-label { color: var(--label-blue); font-weight: 700; font-size: 14.5px; }
  .party-to { right: 345px; text-align: right; }
  .party-from { left: 365px; }

  .credentials { position: absolute; top: 612px; font-size: 12.5px; line-height: 15.5px; }
  .credentials b { color: var(--label-blue); }
  .credentials-license { right: 345px; text-align: right; }
  .credentials-contact { left: 365px; }

  .footer-rule { position: absolute; left: 48px; top: 704px; width: 551px; height: 2px; background: var(--rule); }
  .phone-line { position: absolute; left: 0; width: 100%; top: 728px; text-align: center; font-size: 12.5px; }
  .phone-line b { color: var(--label-green); }
  .phone-line .sep { margin: 0 8px; }

  .letterhead .project { top: 17px; right: 18px; font-size: 7.5px; font-weight: 700; line-height: 9px; }
  .letterhead .project small { display: block; font-weight: 400; font-size: 6.5px; opacity: .85; }
</style>
</head>
<body>
  <section class="page cover">
    <div class="streaks streaks-top" role="img" aria-label="Abstract motion-blur streaks in green, teal and deep blue"></div>
    <div class="streaks streaks-bottom" role="img" aria-label="Abstract motion-blur streaks in green and blue"></div>

    <div class="brand-tab"><span class="brand-dot"></span><span class="brand-name">FROSTLINE<br>CONTRACTING</span></div>

    <h1 class="project project-title">Sample Proposal Title for<br>an Upcoming Project</h1>
    <p class="project project-ref">Ref 091-78956-097</p>
    <p class="project project-date"><strong>March 29, 2011 2:00pm</strong><br>Location Name</p>

    <div class="party party-to">
      <p class="party-label">Prepared for</p>
      <p>Ms. Clara Weston, Director</p>
      <p>Northgate Industries, Inc.</p>
      <p>88 Harbour Road</p>
      <p>Your Town, State, 5555</p>
    </div>
    <div class="party party-from">
      <p class="party-label">Presented by</p>
      <p>Mr. Owen Hale, Director</p>
      <p>Frostline Contracting</p>
      <p>PO Box 5521</p>
      <p>Townsville, Queensland, 4810</p>
    </div>

    <div class="credentials credentials-license">
      <p><b>Electrical Contractors License</b> 12345</p>
      <p><b>KMT</b> 1234567 &nbsp;|&nbsp; <b>VORLE</b> AA12345</p>
    </div>
    <div class="credentials credentials-contact">
      <p><b>E-mail</b>&nbsp; owen@frostline.com.au</p>
      <p><b>Website</b>&nbsp; www.frostline.com.au</p>
    </div>

    <div class="footer-rule"></div>
    <p class="phone-line"><b>Telephone:</b> 07 5550 1820<span class="sep">|</span><b>Fax:</b> 07 5550 1820<span class="sep">|</span><b>Mobile:</b> 0400 555 019</p>
  </section>

  <section class="page letterhead">
    <div class="streaks streaks-top" role="img" aria-label="Abstract motion-blur streaks in green and blue"></div>
    <div class="brand-tab"><span class="brand-dot"></span><span class="brand-name">FROSTLINE<br>CONTRACTING</span></div>
    <p class="project">Sample Proposal Title<br>For an Upcoming Project<small>Ref 091-78956-097</small></p>
  </section>
</body>
</html>
```